Verdane Clinical Spa needs an eye-catching poster to help promote our largest sale of spring!

We need a poster that will go on the back of the doors in the patient rooms. Our medical spa is professional and high-end, so we want the poster to look sophisticated, yet very eye-catching.
This project is for our Marigold Jubilee special, our second largest sale of the year.

Name: Marigold Jubilee
Slogan: Let Your Beauty Bloom
Sale: The More You Buy, The More You Save

Choose from your favorite spa services
NEVRIL, Laser Treatments, Microderms, and More!

It would be great to have something blooming. Flowers, or somehow make a woman look like she's blooming.

I am attaching a visual description of our special. However, the poster should NOT include the pricing tiers. I am also attaching our business logo. Thank you!!

Target Market(s)

A majority are women, but some are men. Around 25-55 in age. Middle to upper class who are likely to spend more money.

Industry/Entity Type

Medical

Font styles to use
Sans Serif
Script

Colors

Designer to choose colors to be used in the design.

Requirements
Must have
• Name of promotion: Marigold Jubilee
• Slogan: "Let Your Beauty Bloom"
• Concept "The more you buy, the more you save on your favorite spa services"
• Select from your favorite spa services such as NEVRIL, laser treatments, microderms, and more!
• Website: VerdaneSpaDeals.com
• Our logo (attached)
Nice to have
• Modern and creative design. Somehow tying in the "Let your beauty bloom" theme. We don't want the focus to be "The more you buy the more you save"
• We are looking for a unique design that is unlike traditional medical spas in the area that typically include a lot of white and a lot of overly photoshopped images.
• Creativity is key! Something that's different than just text and images. We would be so excited to see that!
Should not have
• Not too much text, but enough to get the point across.

```html
<!DOCTYPE html>
<html lang="en">
<head>
<meta charset="utf-8">
<title>Marigold Jubilee – Verdane Clinical Spa</title>
<link rel="stylesheet" href="https://fonts.googleapis.com/css2?family=Arimo:wght@400;600;700&family=Great+Vibes&family=Pacifico&display=swap">
<style>
  :root {
    --page: #ececec;
    --green: #5cb947;
    --green-dark: #3c9a33;
    --green-light: #9bd36a;
    --grey-text: #4a4a4a;
    --title-grey: #6b6b6b;
    --pink: #e0307c;
    --pink-soft: rgba(248, 214, 228, 0.85);
    --white: #ffffff;
    --sky-top: #f7fbff;
    --sky-mid: #dfeaf6;
    --meadow: #8fb46a;
    --meadow-dark: #5f8a45;
    --hair: #c98a5a;
  }
  * { box-sizing: border-box; margin: 0; padding: 0; }
  html, body {
    width: 1200px; height: 1140px; overflow: hidden;
    background: var(--page);
    font-family: "Arimo", Arial, sans-serif;
  }
  .poster {
    position: absolute; left: 210px; top: 28px;
    width: 780px; height: 1084px; overflow: hidden;
    background: var(--white);
    box-shadow: 0 6px 24px rgba(0,0,0,0.18);
  }
  .sky {
    position: absolute; inset: 0 0 430px 0;
    background: linear-gradient(180deg, var(--sky-top) 0%, var(--sky-mid) 55%, #eef3f4 100%);
  }
  .portrait {
    position: absolute; left: 0; right: 0; top: 600px; height: 410px;
    background:
      radial-gradient(ellipse 30% 42% at 46% 68%, var(--hair) 0%, rgba(201,138,90,0.55) 55%, rgba(201,138,90,0) 100%),
      linear-gradient(180deg, #e9eff1 0%, var(--meadow) 38%, var(--meadow-dark) 100%);
  }
  .frame {
    position: absolute; inset: 14px 14px 0 14px;
    border: 2px solid var(--green-light);
    border-bottom: none;
    pointer-events: none;
  }
  .title {
    position: absolute; top: 60px; left: 0; right: 0;
    text-align: center;
  }
  .title-script {
    display: block;
    font-family: "Pacifico", cursive;
    font-size: 124px; line-height: 1.1;
    color: var(--green);
    background: linear-gradient(180deg, var(--green-light) 0%, var(--green) 45%, var(--green-dark) 100%);
    -webkit-background-clip: text; background-clip: text;
    -webkit-text-fill-color: transparent;
    filter: drop-shadow(0 0 2px #fff) drop-shadow(0 0 3px #fff) drop-shadow(2px 4px 4px rgba(0,0,0,0.25));
  }
  .title-caps {
    display: block; margin-top: -14px;
    font-family: "Arimo", Arial, sans-serif; font-weight: 700;
    font-size: 58px; letter-spacing: 2px;
    color: var(--title-grey);
    text-shadow: 0 0 3px #fff, 1px 2px 3px rgba(0,0,0,0.2);
  }
  .slogan {
    position: absolute; top: 312px; left: 0; right: 0;
    text-align: center;
    font-family: "Great Vibes", cursive;
    font-size: 46px; color: var(--pink);
  }
  .rule {
    position: absolute; top: 380px; left: 120px; right: 120px;
    height: 2px;
    background: linear-gradient(90deg, rgba(224,48,124,0), var(--pink) 20%, var(--pink) 80%, rgba(224,48,124,0));
  }
  .offer {
    position: absolute; top: 412px; left: 0; right: 0;
    text-align: center;
    font-size: 33px; line-height: 40px;
    color: var(--grey-text); font-weight: 400;
  }
  .offer strong { color: var(--green); font-weight: 700; }
  .services {
    position: absolute; top: 520px; left: 40px; right: 40px; height: 82px;
    background: linear-gradient(90deg, rgba(248,214,228,0) 0%, var(--pink-soft) 20%, var(--pink-soft) 80%, rgba(248,214,228,0) 100%);
    text-align: center;
    font-size: 22px; line-height: 30px; color: var(--grey-text);
    padding-top: 11px;
  }
  .footer-band {
    position: absolute; left: 0; right: 0; bottom: 0; height: 76px;
    background: var(--green);
  }
  .website {
    position: absolute; left: 60px; bottom: 22px;
    font-size: 30px; color: var(--white); letter-spacing: 0.5px;
  }
  .brand-box {
    position: absolute; left: 508px; bottom: 0;
    width: 180px; height: 98px;
    background: var(--white);
    display: flex; align-items: center; justify-content: center; gap: 8px;
    padding: 0 12px;
  }
  .brand-mark {
    width: 14px; height: 14px; border-radius: 50%;
    background: var(--green); flex: none;
  }
  .brand-name {
    font-family: "Arimo", Arial, sans-serif; font-weight: 600;
    font-size: 20px; line-height: 22px; color: var(--green-dark);
  }
</style>
</head>
<body>
  <main class="poster">
    <div class="sky" role="img" aria-label="Soft cloudy spring sky"></div>
    <div class="portrait" role="img" aria-label="Photo of a woman wearing a crown of white roses and yellow blossoms, looking up, in a green meadow"></div>
    <div class="frame"></div>

    <h1 class="title">
      <span class="title-script">Marigold</span>
      <span class="title-caps">JUBILEE</span>
    </h1>
    <p class="slogan">Let Your Beauty Bloom</p>
    <div class="rule"></div>

    <p class="offer">THE MORE <strong>YOU BUY</strong><br>THE MORE <strong>YOU SAVE</strong></p>

    <p class="services">Choose from your favorite spa services<br>NEVRIL, Laser Treatments, Microderms, and More!</p>

    <footer class="footer-band">
      <span class="website">VerdaneSpaDeals.com</span>
    </footer>
    <div class="brand-box">
      <span class="brand-mark"></span>
      <span class="brand-name">Verdane Clinical Spa</span>
    </div>
  </main>
</body>
</html>
```